Business Card Design

Electrical Contracting buisness
need a buisness card relating to that buisness

Reason: Just need to discuss with partner

Industry/Entity Type

Business

Contact Information for Business Card

Dale Fenwick Electrical
0431 756 918
dalefenwick7@mailnest.example
REC 58714

```html
<!DOCTYPE html>
<html lang="en">
<head>
<meta charset="utf-8">
<title>Dale Fenwick Electrical – Business Card</title>
<link href="https://fonts.googleapis.com/css2?family=Cinzel:wght@600&family=Montserrat:wght@400;600&display=swap" rel="stylesheet">
<style>
  :root {
    --bg: #e6e7ea;
    --card: #ffffff;
    --card-shade: #eef0f3;
    --brand-blue: #2f6fd0;
    --brand-deep: #1f4fa8;
    --brand-sky: #4fb3ee;
    --steel: #9aa2ad;
    --ink: #3a3f47;
    --ink-soft: #6b727c;
  }
  * { box-sizing: border-box; margin: 0; padding: 0; }
  html, body { width: 1200px; height: 901px; overflow: hidden; }
  body {
    background: var(--bg);
    font-family: "Montserrat", sans-serif;
    position: relative;
  }
  .card {
    position: absolute;
    top: 180px;
    width: 340px;
    height: 540px;
    border-radius: 24px;
    background: linear-gradient(160deg, var(--card) 55%, var(--card-shade));
    box-shadow: 0 10px 28px rgba(40, 50, 70, 0.18);
    overflow: hidden;
  }
  .card--front { left: 240px; }
  .card--back { left: 620px; }

  .front-swoosh { position: absolute; left: 0; top: 0; width: 70px; height: 540px; }

  .brand {
    display: flex;
    align-items: center;
    gap: 12px;
  }
  .brand__dot {
    width: 34px; height: 34px;
    border-radius: 50%;
    background: var(--brand-blue);
    flex: none;
  }
  .brand__name {
    font-family: "Cinzel", serif;
    font-weight: 600;
    color: var(--brand-blue);
    line-height: 1.1;
    letter-spacing: 1px;
    white-space: nowrap;
  }
  .card--front .brand { position: absolute; left: 78px; top: 64px; }
  .card--front .brand__name { font-size: 20px; }

  .divider {
    position: absolute;
    left: 78px; top: 160px;
    width: 236px; height: 2px;
    background: linear-gradient(90deg, var(--steel), transparent);
  }

  .contact {
    position: absolute;
    left: 78px; top: 190px;
    width: 240px;
  }
  .contact__name {
    font-weight: 600;
    font-size: 15px;
    color: var(--brand-deep);
    letter-spacing: 0.5px;
  }
  .contact__role { font-size: 11.5px; color: var(--ink-soft); margin-top: 4px; }
  .contact__address { font-size: 11px; color: var(--ink); margin-top: 14px; line-height: 1.5; }
  .contact__list { list-style: none; position: absolute; left: 78px; top: 320px; }
  .contact__list li {
    display: flex; align-items: center; gap: 8px;
    font-size: 11px; color: var(--ink); line-height: 2.1;
  }
  .icon { width: 11px; height: 11px; fill: var(--brand-deep); flex: none; }
  .licence { position: absolute; left: 78px; top: 470px; font-size: 11px; color: var(--ink-soft); letter-spacing: 0.5px; }

  .card--back .brand {
    position: absolute;
    left: 50%; top: 42%;
    transform: translate(-50%, -50%);
  }
  .card--back .brand__dot { width: 40px; height: 40px; }
  .card--back .brand__name { font-size: 24px; }
</style>
</head>
<body>

<section class="card card--front" aria-label="Business card front">
  <svg class="front-swoosh" viewBox="0 0 70 540" aria-hidden="true">
    <defs>
      <linearGradient id="swoosh-blue" x1="0" y1="0" x2="0" y2="1">
        <stop offset="0" stop-color="#1f4fa8"/>
        <stop offset="0.55" stop-color="#4fb3ee"/>
        <stop offset="1" stop-color="#2f6fd0"/>
      </linearGradient>
    </defs>
    <path d="M0 0 V540 H8 C12 380 44 200 28 0 Z" fill="url(#swoosh-blue)"/>
    <path d="M34 0 C50 200 18 380 14 540 H22 C28 380 62 200 46 0 Z" fill="#c3c8cf"/>
  </svg>

  <div class="brand">
    <span class="brand__dot"></span>
    <span class="brand__name">DALE FENWICK<br>ELECTRICAL</span>
  </div>

  <div class="divider"></div>

  <div class="contact">
    <p class="contact__name">OWEN MARSH</p>
    <p class="contact__role">Managing Director</p>
    <p class="contact__address">14 Carver Street, Level 2<br>Harbour Road, UK</p>
  </div>

  <ul class="contact__list">
    <li><svg class="icon" viewBox="0 0 24 24"><path d="M6.6 10.8a15 15 0 0 0 6.6 6.6l2.2-2.2a1 1 0 0 1 1-.25 11.4 11.4 0 0 0 3.6.57 1 1 0 0 1 1 1V20a1 1 0 0 1-1 1A17 17 0 0 1 3 4a1 1 0 0 1 1-1h3.5a1 1 0 0 1 1 1c0 1.25.2 2.45.57 3.57a1 1 0 0 1-.25 1z"/></svg>0431 756 918</li>
    <li><svg class="icon" viewBox="0 0 24 24"><path d="M2 5h20v14H2z M4 7v.5l8 5 8-5V7z" fill-rule="evenodd"/></svg>dalefenwick7@mailnest.example</li>
    <li><svg class="icon" viewBox="0 0 24 24"><circle cx="12" cy="12" r="10"/></svg>dalefenwickelectrical.example</li>
  </ul>

  <p class="licence">REC 58714</p>
</section>

<section class="card card--back" aria-label="Business card back">
  <div class="brand">
    <span class="brand__dot"></span>
    <span class="brand__name">DALE FENWICK<br>ELECTRICAL</span>
  </div>
</section>

</body>
</html>
```